Business card design incorporating discount offer

We are a trade services company and we need a double sided business card that is going to be used by our tradesmen to give to customers on completion of their jobs.

Below are the key elements of the card that we would like to include:

-Main logo with text 'Expert Property Care' underneath.
-Up to 12 smaller icon logos with text 'Your local all-trade experts' to emphasise the point that we cover all the trades
-Discount offer - 10% discount
-Telephone number and website address
-Blank space for tradesman to enter his/her name
-Request for customer feedback with feedback url

This business card will be printed on regular card. In the past we have favoured designs that use a black background but we're open to new ideas.

I have attached a few files:

-A simple wire frame example to show how this card could look with the different elements mentioned above, feel free to use a layout similar to this or come up with something totally different (biz-card.pdf)
-Front and back of a loyalty card the we've used in the past (this card was printed on plastic)
-Front and back of a key fob design that we've previously used (this card was printed on plastic)
-A logo file with the 12 small icons and the main logo image

If you need further images or information please ask.

```html
<!DOCTYPE html>
<html lang="en">
<head>
<meta charset="utf-8">
<title>KTR Expert Property Care – Business Card</title>
<link rel="stylesheet" href="https://fonts.googleapis.com/css2?family=Montserrat:wght@500;600;700;800&display=swap">
<style>
  :root {
    --bg: #2b2b2d;
    --blue-deep: #2a3a98;
    --blue-mid: #1f63c4;
    --blue-light: #3a9ce0;
    --orange: #d58a12;
    --white: #ffffff;
    --ink: #1d1d24;
    --grey: #8a8d92;
    --label-blue: #1f6fc0;
    --font: "Montserrat", Arial, sans-serif;
  }
  * { box-sizing: border-box; margin: 0; padding: 0; }
  html, body { width: 1200px; height: 900px; overflow: hidden; }
  body {
    background: var(--bg);
    font-family: var(--font);
    position: relative;
  }

  .card {
    position: absolute;
    left: 320px;
    width: 560px;
    height: 320px;
    overflow: hidden;
    border-radius: 4px;
    box-shadow: 0 10px 30px rgba(0,0,0,.45);
  }
  .card--front { top: 100px; }
  .card--back  { top: 480px; background: var(--white); }

  /* ---------- Front ---------- */
  .front-main {
    position: absolute; inset: 0 0 122px 0;
    background: linear-gradient(160deg, var(--blue-deep) 0%, var(--blue-mid) 55%, var(--blue-light) 100%);
    padding: 40px 0 0 52px;
    color: var(--white);
  }
  .brand { display: flex; align-items: center; gap: 12px; }
  .brand__mark { width: 44px; height: 44px; background: var(--white); }
  .brand__name { font-size: 58px; font-weight: 800; line-height: 1; letter-spacing: 1px; }
  .brand__tagline { font-size: 22px; font-weight: 700; margin: 8px 0 0 2px; }
  .front-web {
    position: absolute; right: 34px; bottom: 14px;
    font-size: 19px; font-weight: 700; color: var(--white);
  }
  .front-plan {
    position: absolute; left: 0; right: 0; bottom: 70px; height: 52px;
    background: var(--white);
    display: flex; align-items: center; justify-content: flex-end;
    padding-right: 40px;
    font-size: 30px; font-weight: 700; color: var(--ink); letter-spacing: 1px;
  }
  .front-plan .plus { color: var(--label-blue); font-weight: 800; margin-left: 2px; }
  .front-contact {
    position: absolute; left: 0; right: 0; bottom: 0; height: 70px;
    background: var(--orange); color: var(--white);
    display: flex; flex-direction: column; align-items: flex-end; justify-content: center;
    padding-right: 40px;
  }
  .front-contact__note { font-size: 12px; font-weight: 500; }
  .front-contact__phone { font-size: 28px; font-weight: 700; letter-spacing: 2px; }

  /* ---------- Back ---------- */
  .offer {
    position: absolute; left: 0; top: 0; bottom: 0; width: 212px;
    background: linear-gradient(180deg, var(--blue-deep) 0%, var(--blue-mid) 55%, var(--blue-light) 100%);
    color: var(--white); text-align: center;
    padding-top: 22px;
  }
  .offer__value { font-size: 58px; font-weight: 800; line-height: 1; }
  .offer__word { font-size: 29px; font-weight: 800; line-height: 1.05; }
  .offer__plus { display: block; margin: 8px auto; }
  .offer__extra { font-size: 20px; font-weight: 800; line-height: 1.08; }
  .offer__terms { font-size: 11px; font-weight: 600; margin-top: 14px; line-height: 1.3; }
  .stripe {
    position: absolute; left: 212px; top: 0; bottom: 0; width: 16px; background: var(--orange);
  }
  .trades { position: absolute; left: 228px; top: 0; right: 0; bottom: 0; }
  .trade {
    position: absolute; width: 84px;
    display: flex; flex-direction: column; align-items: center; gap: 4px;
    font-size: 11.5px; font-weight: 700; color: var(--label-blue); white-space: nowrap;
  }
  .trade__tile {
    width: 28px; height: 28px; border-radius: 6px;
    display: flex; align-items: center; justify-content: center;
    box-shadow: 0 1px 2px rgba(0,0,0,.25);
  }
  .center-brand {
    position: absolute; left: 96px; top: 132px;
    color: var(--grey);
  }
  .center-brand .brand__mark { width: 32px; height: 32px; background: var(--grey); }
  .center-brand .brand__name { font-size: 40px; }
  .center-brand .brand__tagline { font-size: 14px; font-weight: 700; margin-top: 4px; }
</style>
</head>
<body>

<section class="card card--front" aria-label="Card front">
  <div class="front-main">
    <div class="brand">
      <span class="brand__mark"></span>
      <span class="brand__name">KTR</span>
    </div>
    <p class="brand__tagline">Expert Property Care</p>
    <p class="front-web">www.ktr-services.co.uk</p>
  </div>
  <div class="front-plan">primeCare<span class="plus">+</span></div>
  <div class="front-contact">
    <span class="front-contact__note">Your local property maintenance team</span>
    <span class="front-contact__phone">0800 555 0192</span>
  </div>
</section>

<section class="card card--back" aria-label="Card back">
  <div class="offer">
    <p class="offer__value">10%</p>
    <p class="offer__word">DISCOUNT</p>
    <svg class="offer__plus" width="40" height="40" viewBox="0 0 40 40" aria-hidden="true">
      <rect x="14" y="0" width="12" height="40" fill="#d58a12"/>
      <rect x="0" y="14" width="40" height="12" fill="#d58a12"/>
    </svg>
    <p class="offer__extra">PRIORITY<br>EMERGENCY<br>RESPONSE</p>
    <p class="offer__terms">T&amp;C'S APPLY<br>SEE WEBSITE FOR INFO</p>
  </div>
  <div class="stripe"></div>

  <div class="trades">
    <div class="trade" style="left:0;top:14px">Gas-Heating<span class="trade__tile" style="background:#2b9be0" role="img" aria-label="Gas heating icon"></span></div>
    <div class="trade" style="left:78px;top:30px">Bathrooms<span class="trade__tile" style="background:#c2399b" role="img" aria-label="Bathrooms icon"></span></div>
    <div class="trade" style="left:158px;top:42px">Electricians<span class="trade__tile" style="background:#8a8f96" role="img" aria-label="Electricians icon"></span></div>
    <div class="trade" style="left:246px;top:58px">Building<span class="trade__tile" style="background:#c9853a" role="img" aria-label="Building icon"></span></div>
    <div class="trade" style="left:6px;top:90px">Carpentry<span class="trade__tile" style="background:#d9a02a" role="img" aria-label="Carpentry icon"></span></div>
    <div class="trade" style="left:246px;top:126px">Drainage<span class="trade__tile" style="background:#5b7a94" role="img" aria-label="Drainage icon"></span></div>
    <div class="trade" style="left:0;top:168px"><span class="trade__tile" style="background:#e8c020" role="img" aria-label="Handyman icon"></span>Handyman</div>
    <div class="trade" style="left:242px;top:196px"><span class="trade__tile" style="background:#6cb52e" role="img" aria-label="Pest control icon"></span>Pest-Control</div>
    <div class="trade" style="left:0;top:240px"><span class="trade__tile" style="background:#1d79c4" role="img" aria-label="Plumbing icon"></span>Plumbing</div>
    <div class="trade" style="left:76px;top:250px"><span class="trade__tile" style="background:#2aa6a0" role="img" aria-label="Kitchen icon"></span>Kitchen</div>
    <div class="trade" style="left:154px;top:258px"><span class="trade__tile" style="background:#e0413a" role="img" aria-label="Painting icon"></span>Painting</div>
    <div class="trade" style="left:234px;top:266px"><span class="trade__tile" style="background:#2a6fc0" role="img" aria-label="All trades icon"></span>KTR-All-Trades</div>

    <div class="center-brand">
      <div class="brand">
        <span class="brand__mark"></span>
        <span class="brand__name">KTR</span>
      </div>
      <p class="brand__tagline">Expert Property Care</p>
    </div>
  </div>
</section>

</body>
</html>
```